Quillfield Gallery Ridge Campus

Design cover and inside pages. - will fill in the rest later. I just have some ideas here. This is a marketing brochure for a new building - raising money. Should look professional - but this is an art gallery, so can have color. I wouldn't also mind seeing some chrome effects. I put some samples of fun ideas, but I am open. This is to get people exciting to give to the campaign to raise money for the new building
Target Market(s)
People who would like to donate to a new art gallery - the local community
Requirements
Must have
- The end product, after it is cut down from full bleed, should be 8.25 X 8.25.
Nice to have
- Should be modern and and exciting. The one thing is to show the problem and how we are going to solve it.. Something like "challenge" and resolution"..
- Would like it to go along with this idea of evolve - something new and improved and exciting.. with a very modern look. YOu will see that the logo is three different gradients of orange.. these can change to another color - it doesn't have to be orange.. I would like to see less orange used. The font on the old building is art deco.. so I see that the font for this should be non-serif
Should not have
- I have had designers use the logo as an overlay over pictures - I would like to get away from that.

```html
<!DOCTYPE html>
<html lang="en">
<head>
<meta charset="utf-8">
<title>Quillfield Gallery Ridge Campus — Brochure Spread</title>
<link rel="stylesheet" href="https://fonts.googleapis.com/css2?family=Bowlby+One&family=Open+Sans:wght@400;700;800&display=swap">
<style>
  :root {
    --backdrop: #d9cfca;
    --paper: #ffffff;
    --ink: #111111;
    --body-text: #2a2a2a;
    --folio: #b9b9b9;
    --sky: #2a9fd8;
    --sky-light: #6cc6ee;
    --ember: #e9562a;
    --ember-deep: #d94b22;
    --photo-warm: #8c7d6e;
    --photo-dark: #4b4540;
    --sketch-light: #f4f4f4;
    --sketch-mid: #cfcfcf;
    --plan: #e6e6e6;
    --plan-dark: #8a8a8a;
  }
  * { box-sizing: border-box; margin: 0; padding: 0; }
  html, body { width: 1200px; height: 833px; overflow: hidden; }
  body {
    background: var(--backdrop);
    font-family: "Open Sans", Arial, sans-serif;
    position: relative;
  }
  .spread {
    position: absolute;
    left: 30px; top: 131px;
    width: 1140px; height: 570px;
    display: flex;
  }
  .page {
    position: relative;
    width: 570px; height: 570px;
    background: var(--paper);
    overflow: hidden;
  }
  .page--left { box-shadow: inset -14px 0 18px -14px rgba(0,0,0,.25); }
  .page--right { box-shadow: inset 14px 0 18px -14px rgba(0,0,0,.25); }
  .shapes { position: absolute; inset: 0; }
  .framed {
    position: absolute;
    border: 3px solid var(--ink);
  }
  .photo--garden {
    left: 70px; top: 40px; width: 365px; height: 250px;
    background: linear-gradient(160deg, #b4a597 0%, var(--photo-warm) 40%, var(--photo-dark) 100%);
  }
  .plan {
    background: linear-gradient(90deg, var(--plan-dark) 0%, #b3b3b3 30%, var(--plan) 45%, #f7f7f7 100%);
  }
  .plan--garden { left: 92px; top: 238px; width: 170px; height: 112px; }
  .sketch--reception {
    left: 10px; top: -3px; width: 365px; height: 318px;
    background: linear-gradient(135deg, var(--sketch-light) 0%, #ffffff 45%, var(--sketch-mid) 100%);
  }
  .plan--reception { left: 225px; top: 195px; width: 180px; height: 108px; }
  .title-box {
    position: absolute;
    border: 3px solid var(--ink);
    font-family: "Bowlby One", "Arial Black", sans-serif;
    color: var(--ink);
    text-transform: uppercase;
    line-height: .95;
    font-weight: 400;
  }
  .title-box--garden {
    left: 262px; top: 205px; width: 205px; height: 82px;
    background: linear-gradient(90deg, var(--sky) 0%, var(--sky-light) 100%);
    font-size: 24px;
    padding: 14px 0 0 18px;
  }
  .title-box--reception {
    left: 60px; top: 282px; width: 210px; height: 50px;
    background: var(--paper);
    font-size: 27px;
    padding: 7px 0 0 12px;
  }
  .copy {
    position: absolute;
    font-size: 8.8px;
    line-height: 1.3;
    color: var(--body-text);
  }
  .copy p + p { margin-top: 6px; }
  .copy h2 {
    font-size: 12px;
    font-weight: 800;
    color: var(--ink);
    margin-bottom: 3px;
  }
  .folio {
    position: absolute;
    font-size: 8px;
    color: var(--folio);
  }
</style>
</head>
<body>
<main class="spread">

  <section class="page page--left" aria-label="Sculpture Garden">
    <svg class="shapes" width="570" height="570" viewBox="0 0 570 570" aria-hidden="true">
      <polygon points="0,215 270,215 270,360 0,375" fill="var(--sky)"/>
      <line x1="0" y1="215" x2="270" y2="215" stroke="var(--ink)" stroke-width="3"/>
      <line x1="0" y1="375" x2="270" y2="360" stroke="var(--ink)" stroke-width="3"/>
      <polygon points="475,20 570,10 570,300 475,300" fill="var(--ember)"/>
      <line x1="475" y1="20" x2="475" y2="300" stroke="var(--ink)" stroke-width="3"/>
    </svg>
    <div class="framed photo--garden" role="img" aria-label="Rendering of the sculpture garden courtyard with seating, trees and an iron fence"></div>
    <div class="framed plan plan--garden" role="img" aria-label="Floor plan of the sculpture garden"></div>
    <h1 class="title-box title-box--garden">Sculpture<br>Garden</h1>

    <div class="copy" style="left:40px; top:385px; width:225px;">
      <p>Lorem ipsum dolor sit amet, consectetur adipiscing elit. Ut nibh leo, cursus et laoreet ac, lobortis vulputate orci.</p>
      <p>Nunc ultricies massa egestas malesuada pretium. Morbi congue sem ultricies dui lobortis dictum. Ut convallis quam diam, vel interdum dolor semper et. Morbi tincidunt fermentum sem sit amet iaculis.</p>
      <p>Sed ullamcorper egestas metus, quis luctus magna venenatis id. Aenean ultricies enim eget magna convallis, aliquet venenatis nisi varius. Sed varius eu lectus nec ullamcorper. Praesent ullamcorper, nulla sed lobortis ultrices, urna mi tincidunt.</p>
    </div>
    <div class="copy" style="left:285px; top:305px; width:235px;">
      <p>Sed ullamcorper egestas metus, quis luctus magna venenatis id. Aenean ultricies enim eget magna convallis, aliquet venenatis nisi varius. Sed varius eu lectus nec ullam corper. Praesent ullamcorper, nulla sed lobortis ultrices, urna mi tincidunt.</p>
      <p>Nunc ultricies massa egestas malesuada pretium. Morbi congue sem ultricies dui lobortis dictum. Ut convallis quam diam, vel interdum dolor semper et. Morbi tincidunt fermentum sem sit amet iaculis.</p>
      <p>Lorem ipsum dolor sit amet, consectetur adipiscing elit. Ut nibh leo, cursus et laoreet ac, lobortis vulputate orci.</p>
    </div>
    <span class="folio" style="left:470px; top:535px;">Page 1 of 4</span>
  </section>

  <section class="page page--right" aria-label="Reception">
    <svg class="shapes" width="570" height="570" viewBox="0 0 570 570" aria-hidden="true">
      <polygon points="0,10 12,10 12,300 0,300" fill="var(--ember)"/>
      <polygon points="375,30 570,20 570,255 375,260" fill="var(--ember-deep)"/>
      <line x1="375" y1="30" x2="570" y2="20" stroke="var(--ink)" stroke-width="3"/>
      <line x1="375" y1="260" x2="570" y2="255" stroke="var(--ink)" stroke-width="3"/>
    </svg>
    <div class="framed sketch--reception" role="img" aria-label="Line drawing of the reception area with a glass facade and welcome signage"></div>
    <div class="framed plan plan--reception" role="img" aria-label="Floor plan of the reception area"></div>
    <h1 class="title-box title-box--reception">Reception</h1>

    <div class="copy" style="left:55px; top:342px; width:225px;">
      <h2>Challenge</h2>
      <p>Lorem ipsum dolor sit amet, consectetur adipiscing elit. Ut nibh leo, cursus et laoreet ac, lobortis vulputate orci.</p>
      <p>Nunc ultricies massa egestas malesuada pretium. Morbi congue sem ultricies dui lobortis dictum. Ut convallis quam diam, vel interdum dolor semper et. Morbi tincidunt fermentum sem sit amet iaculis.</p>
      <p>Sed ullamcorper egestas metus, quis luctus magna venenatis id. Aenean ultricies enim eget magna convallis, aliquet venenatis nisi varius. Sed varius eu lectus nec.</p>
    </div>
    <div class="copy" style="left:300px; top:318px; width:235px;">
      <h2>Resolution</h2>
      <p>Sed ullamcorper egestas metus, quis luctus magna venenatis id. Aenean ultricies enim eget magna convallis, aliquet venenatis nisi varius. Sed varius eu lectus nec ullam corper. Praesent ullamcorper, nulla sed lobortis ultrices, urna mi tincidunt.</p>
      <p>Nunc ultricies massa egestas malesuada pretium. Morbi congue sem ultricies dui lobortis dictum. Ut convallis quam diam, vel interdum dolor semper et. Morbi tincidunt fermentum sem sit amet iaculis.</p>
    </div>
    <span class="folio" style="left:55px; top:535px;">Page 2 of 4</span>
  </section>

</main>
</body>
</html>
```